BRANWELL LAW FIRM

Seeking a business logo and business card design incorporating the logo. We have an existing business card (attached), which we would like redesigned incorporating the new logo and existing text (front and back). Also, logo and business card should incorporate the same color scheme as on the attached. There are several employees who will need business cards; not sure how this is handled from a business card design standpoint . . . please contact me with any questions/concerns.

Please feel free to redesign front of business card. Branwell Law Firm must read Branwell Law Firm, P.C.

Back of business card should have the below address information towards the bottom of the card, so there is room for someone to write on the back. The address information on the back of the business cards is as follows:

Three Larchmont Court Plaza
2700 Quillan Boulevard, Suite 1140
Philadelphia, PA 19388
T: (215) 555.0143

68 Tarrow Avenue, 24th Floor
New York, NY 10099
T: (212) 555-0182

Industry/Entity Type

Business

Logo Text

BLF

```html
<!DOCTYPE html>
<html lang="en">
<head>
<meta charset="utf-8">
<title>Branwell Law Firm, P.C. — Identity</title>
<link rel="stylesheet" href="https://fonts.googleapis.com/css2?family=Cinzel:wght@400&family=Raleway:wght@400;600&display=swap">
<style>
  :root {
    --navy: #323e4e;
    --silver: #d2d2d2;
    --silver-soft: #c4c8ce;
    --faint-mark: #424e5f;
    --divider: #9a9a9a;
    --paper: #ffffff;
  }
  * { margin: 0; padding: 0; box-sizing: border-box; }
  html, body { width: 1200px; height: 1000px; overflow: hidden; background: var(--paper); }
  .canvas { position: relative; width: 1200px; height: 1000px; }

  .brand-panel {
    position: absolute; left: 0; top: 0; width: 1200px; height: 540px;
    background: var(--navy);
  }
  .panel-rule {
    position: absolute; left: 0; top: 540px; width: 1200px; height: 8px;
    background: var(--divider);
  }
  .monogram {
    position: absolute; left: 0; width: 100%; text-align: center;
    font-family: "Cinzel", serif; font-weight: 400; color: var(--silver);
    line-height: 1;
  }
  .brand-panel .monogram { top: 180px; font-size: 120px; }
  .firm-name {
    position: absolute; left: 0; width: 100%; text-align: center;
    font-family: "Cinzel", serif; font-weight: 400; color: var(--silver);
    line-height: 1;
  }
  .brand-panel .firm-name { top: 362px; font-size: 40px; letter-spacing: 1px; }

  .card {
    position: absolute; top: 653px; width: 468px; height: 267px;
    background: var(--navy); overflow: hidden;
  }
  .card-front { left: 90px; }
  .card-back { left: 640px; }

  .card-front .monogram { top: 30px; font-size: 44px; }
  .card-front .firm-name { top: 758px; }
  .card .firm-name { top: 106px; font-size: 19px; }
  .card-rule { position: absolute; height: 1px; background: var(--silver-soft); }
  .rule-upper { left: 90px; width: 288px; top: 131px; }
  .rule-lower { left: 117px; width: 234px; top: 193px; }
  .person-name {
    position: absolute; top: 146px; width: 100%; text-align: center;
    font-family: "Raleway", sans-serif; font-size: 19px; color: var(--silver);
    letter-spacing: 0.5px;
  }
  .person-name strong { font-weight: 600; }
  .person-title {
    position: absolute; top: 173px; width: 100%; text-align: center;
    font-family: "Raleway", sans-serif; font-size: 8.5px; color: var(--silver-soft);
    letter-spacing: 1px; text-transform: uppercase;
  }
  .contact {
    position: absolute; top: 203px; width: 100%; text-align: center;
    font-family: "Raleway", sans-serif; font-size: 9px; color: var(--silver-soft);
    letter-spacing: 1px; line-height: 15px;
  }
  .contact .gap { display: inline-block; width: 14px; }

  .card-back .monogram { top: 85px; font-size: 78px; color: var(--faint-mark); }
  .addresses {
    position: absolute; top: 221px; width: 100%; text-align: center;
    font-family: "Raleway", sans-serif; font-size: 7px; color: var(--silver-soft);
    letter-spacing: 0.3px; line-height: 13px; white-space: nowrap;
  }
  .addresses .gap { display: inline-block; width: 6px; }
</style>
</head>
<body>
<div class="canvas">
  <section class="brand-panel">
    <div class="monogram">BLF</div>
    <div class="firm-name">Branwell Law Firm, P.C.</div>
  </section>
  <div class="panel-rule"></div>

  <article class="card card-front">
    <div class="monogram">BLF</div>
    <div class="firm-name" style="top:106px">Branwell Law Firm, P.C.</div>
    <div class="card-rule rule-upper"></div>
    <div class="person-name"><strong>Martin</strong> J. Ressler</div>
    <div class="person-title">Director Business Development</div>
    <div class="card-rule rule-lower"></div>
    <div class="contact">
      mressler@branwelllawfirm.com<br>
      mobile : 215.555.0177<span class="gap"></span>www.branwelllawfirm.com<br>
      Philadelphia, PA<span class="gap"></span>New York, NY
    </div>
  </article>

  <article class="card card-back">
    <div class="monogram">BLF</div>
    <div class="addresses">
      Three Larchmont Court Plaza<span class="gap"></span>2700 Quillan Boulevard, Suite 1140<span class="gap"></span>Philadelphia, PA 19388<span class="gap"></span>T: (215) 555.0143<br>
      68 Tarrow Avenue, 24th Floor<span class="gap"></span>New York, NY 10099<span class="gap"></span>T: (212) 555-0182
    </div>
  </article>
</div>
</body>
</html>
```